Landing Page - Lending & Lantern

Need a singular landing page that will eventually link to podcast and direct people to my page. I need it to work with TallyMorrow.

The page is geared about small business owners and linking them with high quality banker to obtain financing. It should be professional, connect to bourbon as an underlying tone. It's all about qualify and integrity.

It needs to be put in Wordpress.
I don't know the difference between coded and uncoded, I just want it done.

Target Market(s)

Business Owners and those needing help with financing. The people we're trying to help aren't rich, they are successful but need help.

Industry/Entity Type

Finance & Bourbon

Coding

Coded - Design and coding required

Number of Pages Required

1 page

Colors
0054AA
0677BA
7BADD7
CADEEF
E8F1F8
0094D4
00A9DD
6FCCEA
C7EBF8
E9F6FB

Requirements
Must have
• Link to send email
Nice to have
• Use colors and fonts in branding.

```html
<!DOCTYPE html>
<html lang="en">
<head>
<meta charset="utf-8">
<title>Lending &amp; Lantern</title>
<link href="https://fonts.googleapis.com/css2?family=Arvo:wght@400;700&family=Poppins:wght@400;500;600;700&display=swap" rel="stylesheet">
<style>
:root{
  --teal:#13a39b;
  --dark:#2b2b2b;
  --darker:#1d1d1d;
  --ink:#1a1a1a;
  --text:#555;
  --card:#f1f1f1;
  --white:#fff;
  --rule:#c9c9c9;
}
*{margin:0;padding:0;box-sizing:border-box}
html,body{width:1200px;height:4218px;overflow:hidden}
body{position:relative;background:var(--white);font-family:"Poppins",sans-serif;color:var(--text)}
a{color:inherit;text-decoration:none}
.abs{position:absolute}
.slab{font-family:"Arvo",serif}

/* header */
.site-header{position:absolute;left:0;top:0;width:1200px;height:105px;background:var(--dark);z-index:5}
.nav{position:absolute;top:0;height:105px;display:flex;align-items:center;gap:27px;font-family:"Arvo",serif;font-size:16px;color:var(--white)}
.nav-left{left:79px}
.nav-right{left:725px}
.nav .active{color:var(--teal)}
.nav-phone{color:var(--teal);font-family:"Poppins",sans-serif;font-size:19px;display:flex;align-items:center;gap:8px;margin-left:6px}
.brand-badge{position:absolute;left:492px;top:0;width:216px;height:172px;border-radius:0 0 108px 108px;background:var(--dark);display:flex;flex-direction:column;align-items:center;justify-content:center;z-index:6}
.brand-badge span{font-family:"Arvo",serif;font-weight:700;font-size:30px;line-height:1.05;color:var(--white);text-align:center}

/* hero */
.hero{position:absolute;left:0;top:105px;width:1200px;height:697px;background:linear-gradient(160deg,#6d7a82 0%,#3a3f44 45%,#24272a 100%)}
.hero-curve{position:absolute;left:0;top:0;width:1200px;height:697px}
.hero-title{position:absolute;left:0;top:330px;width:1200px;text-align:center;font-family:"Arvo",serif;font-weight:700;font-size:68px;letter-spacing:2px;color:var(--white)}
.hero-sub{position:absolute;left:0;top:413px;width:1200px;text-align:center;font-weight:700;font-size:21px;line-height:31px;color:var(--white)}
.btn{position:absolute;width:188px;height:52px;border-radius:26px;display:flex;align-items:center;justify-content:center;font-family:"Arvo",serif;font-size:17px;color:var(--white)}
.btn-teal{background:var(--teal)}
.btn-dark{background:var(--ink)}

/* welcome */
.welcome-ring{position:absolute;left:73px;top:893px;width:516px;height:516px;border-radius:50%;border:8px solid var(--ink);box-shadow:inset 0 0 0 8px var(--teal)}
.welcome-photo{position:absolute;left:97px;top:917px;width:468px;height:468px;border-radius:50%;background:linear-gradient(135deg,#c9b7a6,#7f6a5b 55%,#3d4a5e)}
.h2{font-family:"Arvo",serif;font-size:44px;line-height:48px;color:var(--ink);text-transform:uppercase}
.welcome-title{left:615px;top:944px}
.welcome-title em{font-style:normal;color:var(--teal);display:block}
.body-copy{font-size:15.5px;line-height:30.3px}
.welcome-copy{left:615px;top:1052px;width:510px}

/* what we do */
.what-band{position:absolute;left:0;top:1495px;width:1200px;height:543px;background:var(--teal)}
.what-title{left:74px;top:1570px;color:var(--white)}
.what-copy{left:74px;top:1632px;width:430px;color:var(--white)}
.what-photo{position:absolute;left:524px;top:1568px;width:601px;height:396px;border-radius:65px;background:linear-gradient(135deg,#d9d2c4,#8d8e8c 50%,#3e4f6a)}

/* section heads */
.sec-head{position:absolute;left:74px;display:flex;align-items:center;width:1052px}
.sec-head .h2{white-space:nowrap}
.sec-head .rule{flex:1;height:1px;background:var(--rule);margin:0 40px 0 22px}
.sec-head .arrows{display:flex;gap:22px}

/* podcast cards */
.pod-card{position:absolute;top:2189px;width:242px;height:343px;background:var(--card)}
.pod-img{width:242px;height:180px;position:relative}
.pod-mic{position:absolute;left:12px;bottom:8px;width:24px;height:24px;border-radius:50%;background:var(--teal)}
.pod-body{padding:13px 15px 0}
.pod-time{font-size:13px;font-weight:500;color:var(--ink)}
.card-title{font-family:"Arvo",serif;font-weight:700;font-size:18.5px;color:var(--teal);margin-top:5px}
.card-text{font-size:14.5px;line-height:25.5px;color:var(--text);margin-top:4px}

/* testimonials */
.testi{position:absolute;left:0;top:2603px;width:1200px;height:597px}
.testi-title{left:0;top:2724px;width:1200px;text-align:center;color:var(--white)}
.avatar-ring{position:absolute;left:166px;top:2803px;width:196px;height:196px;border-radius:50%;border:5px solid var(--teal);box-shadow:inset 0 0 0 5px var(--ink)}
.avatar{position:absolute;left:178px;top:2815px;width:172px;height:172px;border-radius:50%;background:linear-gradient(135deg,#e6e2dc,#8e8a86 60%,#30343a)}
.testi-quote{left:403px;top:2802px;width:640px;color:var(--white)}
.testi-name{left:403px;top:2968px;font-family:"Arvo",serif;font-weight:700;font-size:18.5px;color:var(--teal)}

/* news cards */
.news-card{position:absolute;top:3294px;width:329px;height:381px;background:var(--card)}
.news-img{width:329px;height:198px}
.news-body{padding:18px 18px 0}
.read-more{display:inline-block;margin-top:12px;font-size:14.5px;font-weight:600;color:var(--ink);text-decoration:underline}

/* footer */
.site-footer{position:absolute;left:0;top:3798px;width:1200px;height:420px}
.footer-brand{position:absolute;left:74px;top:3905px;width:242px;font-family:"Arvo",serif;font-weight:700;font-size:36px;line-height:44px;color:#b9b9b9;text-align:center}
.f-col{position:absolute;top:3851px;color:var(--white);font-size:16.5px}
.f-col h3{font-family:"Arvo",serif;font-weight:700;font-size:21px;color:var(--teal);margin-bottom:10px}
.f-col li{list-style:none;line-height:37px}
.contact-row{display:flex;gap:14px;align-items:flex-start;line-height:26px;margin-bottom:10px}
.contact-row svg{flex:none;margin-top:6px}
.footer-bar{position:absolute;left:0;top:4150px;width:1200px;height:68px;background:var(--darker)}
.copyright{position:absolute;left:74px;top:4175px;font-size:14px;color:var(--white)}
.socials{position:absolute;left:944px;top:4172px;display:flex;gap:18px}
.socials span{width:22px;height:22px;border-radius:50%;background:var(--white);display:block}
</style>
</head>
<body>

<header class="site-header">
  <nav class="nav nav-left">
    <a class="active" href="#">Home</a>
    <a href="#">Who We Are</a>
    <a href="#">What We Do</a>
    <a href="#">Podcasts</a>
  </nav>
  <nav class="nav nav-right">
    <a href="#">Latest News</a>
    <a href="mailto:hello@lendinglantern.com">Contact Us</a>
    <span class="nav-phone">
      <svg width="16" height="16" viewBox="0 0 24 24"><path fill="#13a39b" d="M6.6 10.8a15.1 15.1 0 0 0 6.6 6.6l2.2-2.2a1 1 0 0 1 1-.25 11.4 11.4 0 0 0 3.6.57 1 1 0 0 1 1 1V20a1 1 0 0 1-1 1A17 17 0 0 1 3 4a1 1 0 0 1 1-1h3.5a1 1 0 0 1 1 1c0 1.25.2 2.45.57 3.57a1 1 0 0 1-.25 1z"/></svg>
      +1 555-014-2270
    </span>
  </nav>
</header>
<div class="brand-badge"><span>Lending &amp;<br>Lantern</span></div>

<section class="hero" role="img" aria-label="Three businessmen in suits talking over glasses of bourbon at a bar">
  <svg class="hero-curve" viewBox="0 0 1200 697" aria-hidden="true"><path d="M0 607 Q600 787 1200 607 L1200 697 L0 697Z" fill="#fff"/></svg>
</section>
<h1 class="hero-title">LENDING AND LANTERN</h1>
<p class="hero-sub">Neque porro quisquam est qui dolorem ipsum quia dolor sit laboris<br>nisi ut aliquip ex ea commodo consequa .</p>
<a class="btn btn-teal" style="left:506px;top:598px" href="#">READ MORE</a>

<div class="welcome-ring"></div>
<div class="welcome-photo" role="img" aria-label="A banker and a business owner reviewing documents at a desk"></div>
<h2 class="h2 abs welcome-title">Welcome to<em>Lending &amp; Lantern</em></h2>
<p class="body-copy abs welcome-copy">Sed ut perspiciatis unde omnis iste natus error sit &nbsp;voluptatem accusantium doloremque laudantium, totam rem aperiam, eaque ipsa quae ab illo inventore veritatis et quasi architecto beatae vitae dicta sunt explicabo. Nemo enim ipsam voluptatem quia &nbsp;voluptas sit aspernatur aut odit aut fugit, sed quia consequuntur magni dolores eos qui ratione &nbsp;voluptatem sequi nesciunt.</p>
<a class="btn btn-dark" style="left:615px;top:1297px" href="#">READ MORE</a>

<section class="what-band"></section>
<h2 class="h2 abs what-title">What we do</h2>
<p class="body-copy abs what-copy">Sed ut perspiciatis unde omnis iste natus error sit voluptatem accusantium doloremque laudantium, totam rem aperiam, eaque ipsa quae ab illo inventore veritatis et quasi architecto beatae vitae dicta sunt explicabo. Nemo enim ipsam voluptatem quia voluptas sit aspernatur aut odit aut fugit, sed quia consequuntur magni dolores eos qui ratione voluptatem sequi nesciunt.</p>
<a class="btn btn-dark" style="left:74px;top:1901px" href="#">READ MORE</a>
<div class="what-photo" role="img" aria-label="A banker reviewing a clipboard with two workers in a warehouse"></div>

<div class="sec-head" style="top:2104px">
  <h2 class="h2">Podcasts</h2><span class="rule"></span>
  <span class="arrows">
    <svg width="16" height="26" viewBox="0 0 16 26"><path d="M13 3 3 13l10 10" fill="none" stroke="#333" stroke-width="2.5"/></svg>
    <svg width="16" height="26" viewBox="0 0 16 26"><path d="m3 3 10 10L3 23" fill="none" stroke="#13a39b" stroke-width="2.5"/></svg>
  </span>
</div>

<article class="pod-card" style="left:74px">
  <div class="pod-img" role="img" aria-label="Two podcast hosts talking at microphones" style="background:linear-gradient(135deg,#d8cbb7,#8a7763 60%,#4d4238)"><span class="pod-mic"></span></div>
  <div class="pod-body"><div class="pod-time">32Mins</div><div class="card-title">Sed ut perspiciatis</div><p class="card-text">Unde omnis iste natuserror sit &nbsp;voluptatem accusan tium doloremque.</p></div>
</article>
<article class="pod-card" style="left:345px">
  <div class="pod-img" role="img" aria-label="A woman recording a podcast with headphones" style="background:linear-gradient(135deg,#e0d6c8,#a9876b 60%,#5b4636)"><span class="pod-mic"></span></div>
  <div class="pod-body"><div class="pod-time">32Mins</div><div class="card-title">Sed ut perspiciatis</div><p class="card-text">Unde omnis iste natuserror sit &nbsp;voluptatem accusan tium doloremque.</p></div>
</article>
<article class="pod-card" style="left:615px">
  <div class="pod-img" role="img" aria-label="Two people recording an interview in a bright studio" style="background:linear-gradient(135deg,#eef0f1,#b9c0c6 55%,#55606b)"><span class="pod-mic"></span></div>
  <div class="pod-body"><div class="pod-time">32Mins</div><div class="card-title">Sed ut perspiciatis</div><p class="card-text">Unde omnis iste natuserror sit &nbsp;voluptatem accusan tium doloremque.</p></div>
</article>
<article class="pod-card" style="left:885px">
  <div class="pod-img" role="img" aria-label="Close-up of a studio microphone" style="background:linear-gradient(135deg,#f2efe9,#b8b2a8 50%,#2c2c2c)"><span class="pod-mic"></span></div>
  <div class="pod-body"><div class="pod-time">32Mins</div><div class="card-title">Sed ut perspiciatis</div><p class="card-text">Unde omnis iste natuserror sit &nbsp;voluptatem accusan tium doloremque.</p></div>
</article>

<section class="testi">
  <svg width="1200" height="597" viewBox="0 0 1200 597" aria-hidden="true"><path d="M0 98 Q600 -98 1200 98 L1200 597 Q600 517 0 597Z" fill="#2b2b2b"/></svg>
</section>
<h2 class="h2 abs testi-title">Testimonials</h2>
<svg class="abs" style="left:122px;top:2888px" width="16" height="26" viewBox="0 0 16 26"><path d="M13 3 3 13l10 10" fill="none" stroke="#fff" stroke-width="2.5"/></svg>
<svg class="abs" style="left:1063px;top:2888px" width="16" height="26" viewBox="0 0 16 26"><path d="m3 3 10 10L3 23" fill="none" stroke="#fff" stroke-width="2.5"/></svg>
<div class="avatar-ring"></div>
<div class="avatar" role="img" aria-label="Portrait of a smiling client in a suit"></div>
<p class="body-copy abs testi-quote">“ Sed ut perspiciatis unde omnis iste natus error sit &nbsp;voluptatem accusantium doloremque laudantium, totam rem aperiam, eaque ipsa quae ab illo inventore veritatis et quasi architecto beatae vitae dicta sunt explicabo. Nemo enim ipsam voluptatem quia &nbsp;voluptas sit aspernatur aut odit aut fugit, sed quia conseq uuntur magni dolores eos qui ratione voluptatem sequi nesciunt...”</p>
<div class="abs testi-name">-Name Heading</div>

<div class="sec-head" style="top:3209px">
  <h2 class="h2">Latest News</h2><span class="rule"></span>
  <span class="arrows">
    <svg width="16" height="26" viewBox="0 0 16 26"><path d="M13 3 3 13l10 10" fill="none" stroke="#333" stroke-width="2.5"/></svg>
    <svg width="16" height="26" viewBox="0 0 16 26"><path d="m3 3 10 10L3 23" fill="none" stroke="#13a39b" stroke-width="2.5"/></svg>
  </span>
</div>

<article class="news-card" style="left:74px">
  <div class="news-img" role="img" aria-label="A smiling businessman in a meeting room" style="background:linear-gradient(135deg,#dcdcd8,#8b8f94 55%,#2f3b52)"></div>
  <div class="news-body"><div class="card-title">Sed ut perspiciatis</div><p class="card-text">Unde omnis iste natuserror sitvol tatem accusan tium doloremque dolore eu fugiat nulla.</p><a class="read-more" href="#">Read More</a></div>
</article>
<article class="news-card" style="left:436px">
  <div class="news-img" role="img" aria-label="Hands reviewing financial charts on paper and a tablet" style="background:linear-gradient(135deg,#e9edf1,#9fb1c3 55%,#3b5168)"></div>
  <div class="news-body"><div class="card-title">Sed ut perspiciatis</div><p class="card-text">Unde omnis iste natuserror sitvol tatem accusan tium doloremque dolore eu fugiat nulla.</p><a class="read-more" href="#">Read More</a></div>
</article>
<article class="news-card" style="left:797px">
  <div class="news-img" role="img" aria-label="A client and an advisor talking across a desk with a laptop" style="background:linear-gradient(135deg,#f1eee9,#c3b9ad 55%,#4a4a4a)"></div>
  <div class="news-body"><div class="card-title">Sed ut perspiciatis</div><p class="card-text">Unde omnis iste natuserror sitvol tatem accusan tium doloremque dolore eu fugiat nulla.</p><a class="read-more" href="#">Read More</a></div>
</article>

<footer class="site-footer">
  <svg width="1200" height="420" viewBox="0 0 1200 420" aria-hidden="true"><path d="M0 0 Q600 74 1200 0 L1200 420 L0 420Z" fill="#2b2b2b"/></svg>
</footer>
<div class="footer-brand">Lending &amp;<br>Lantern</div>
<div class="f-col" style="left:367px">
  <h3>Site Map</h3>
  <ul><li>Home</li><li>Who We Are</li><li>What We Do</li><li>Podcasts</li><li>Latest News</li><li>Contact Us</li></ul>
</div>
<div class="f-col" style="left:596px">
  <h3>Resources</h3>
  <ul><li>Sed ut perspiciatis</li><li>Unde omnis iste</li><li>Natus error</li><li>Sit voluptatem acc</li><li>Asantium</li></ul>
</div>
<div class="f-col" style="left:856px">
  <h3>Contact Us</h3>
  <div class="contact-row">
    <svg width="18" height="16" viewBox="0 0 24 20"><path fill="#13a39b" d="M12 0a7 7 0 0 0-7 7c0 5 7 13 7 13s7-8 7-13a7 7 0 0 0-7-7zm0 9.5A2.5 2.5 0 1 1 12 4.5a2.5 2.5 0 0 1 0 5z"/></svg>
    <span>48 Harrow Lane Suite 12,<br>Dunmore 40112, United States</span>
  </div>
  <div class="contact-row">
    <svg width="18" height="16" viewBox="0 0 24 24"><path fill="#13a39b" d="M6.6 10.8a15.1 15.1 0 0 0 6.6 6.6l2.2-2.2a1 1 0 0 1 1-.25 11.4 11.4 0 0 0 3.6.57 1 1 0 0 1 1 1V20a1 1 0 0 1-1 1A17 17 0 0 1 3 4a1 1 0 0 1 1-1h3.5a1 1 0 0 1 1 1c0 1.25.2 2.45.57 3.57a1 1 0 0 1-.25 1z"/></svg>
    <span>+1 555-014-2270</span>
  </div>
  <div class="contact-row">
    <svg width="18" height="14" viewBox="0 0 24 18"><path fill="#13a39b" d="M0 0h24v18H0z"/><path d="M1 1l11 8 11-8" fill="none" stroke="#2b2b2b" stroke-width="2"/></svg>
    <a href="mailto:hello@lendinglantern.com">hello@lendinglantern.com</a>
  </div>
</div>
<div class="footer-bar"></div>
<p class="copyright">Copyright © 2023 Lending &amp; Lantern &nbsp;All Rights Reserved</p>
<div class="socials" aria-label="Social links"><span></span><span></span><span></span><span></span><span></span></div>

</body>
</html>
```